Dance school needs a poster to promote our annual concert

I have a dance school called 'The Marisol Kemp Dancers'
See designs from previous years
This year's concert theme is Hobart Pemberly animation movies
The title of the concert is "wondRix"
Dance items will be choreographed to; “Drowsy Maiden”, Tidal Sprite”, “The Nine Gnomes”, “The Fox Regent”, “Corvan”, “Rosalind & the Ogre” & “Glimmerwisp”.
I need a colorful A4 (portrait) poster promoting the concert.

Target Market(s)

Families of students & dance community

Industry/Entity Type

Dance Studio

Font styles to use
Other font styles liked:
• "Mistral" for my my name (see examples supplied)

Colors

Designer to choose colors to be used in the design.

Requirements
Must have
• Must Have:
• - The poster must include the following information:
• 'The Marisol Kemp Dancers'
• presents
• "wondRix"
• (Font for my name is "Mistral")
• Saturday 25th November 2017
• Brisket Theatre,
• Holloway College Brambledale.

```html
<!DOCTYPE html>
<html lang="en">
<head>
<meta charset="utf-8">
<title>wondRix – The Marisol Kemp Dancers</title>
<link rel="stylesheet" href="https://fonts.googleapis.com/css2?family=Kaushan+Script&family=Cinzel:wght@600;700;900&display=swap">
<style>
  :root {
    --page-bg: #2a2a2e;
    --poster-black: #050505;
    --name-magenta: #d63ad8;
    --title-ink: #fbe6ff;
    --info-white: #f4f4f4;
    --glow-pink: #e0307a;
    --glow-purple: #5a1a6e;
    --glow-gold: #f2b640;
    --glow-deep: #120418;
  }
  * { margin: 0; padding: 0; box-sizing: border-box; }
  html, body {
    width: 1200px; height: 800px; overflow: hidden;
    background: var(--page-bg);
  }
  .poster {
    position: absolute; left: 340px; top: 30px;
    width: 520px; height: 740px;
    background: var(--poster-black);
    overflow: hidden;
  }
  .poster__artwork {
    position: absolute; inset: 0;
    background:
      radial-gradient(ellipse 45% 30% at 45% 70%, var(--glow-gold) 0%, transparent 70%),
      radial-gradient(ellipse 55% 45% at 70% 25%, var(--glow-pink) 0%, transparent 75%),
      radial-gradient(ellipse 60% 50% at 40% 45%, var(--glow-purple) 0%, transparent 80%),
      var(--glow-deep);
  }
  .poster__name-band {
    position: absolute; left: 0; right: 0; top: 38px; height: 74px;
    background: var(--poster-black);
    display: flex; align-items: center; justify-content: center;
  }
  .poster__name {
    font-family: "Kaushan Script", cursive;
    font-weight: 400;
    font-size: 40px;
    color: var(--name-magenta);
    white-space: nowrap;
  }
  .poster__presents {
    position: absolute; left: 24px; top: 112px;
    font-family: "Cinzel", serif; font-weight: 700;
    font-size: 19px; letter-spacing: 0.5px;
    color: var(--info-white);
  }
  .poster__title {
    position: absolute; left: 0; right: 0; top: 355px;
    text-align: center;
    font-family: "Cinzel", serif; font-weight: 900;
    font-size: 72px; line-height: 1;
    letter-spacing: 4px;
    text-transform: uppercase;
    color: var(--title-ink);
  }
  .poster__details {
    position: absolute; left: 0; right: 0; bottom: 0; height: 122px;
    background: var(--poster-black);
    display: flex; flex-direction: column; align-items: center; justify-content: center;
    font-family: "Cinzel", serif; font-weight: 600;
    font-size: 23px; line-height: 29px;
    color: var(--info-white);
    text-align: center;
    white-space: nowrap;
  }
</style>
</head>
<body>
  <main class="poster">
    <div class="poster__artwork" role="img" aria-label="Photo of a dancer with flowing hair amid glowing pink, purple and gold light streaks and sparkles"></div>
    <div class="poster__name-band">
      <h2 class="poster__name">The Marisol Kemp Dancers</h2>
    </div>
    <p class="poster__presents">Presents</p>
    <h1 class="poster__title">wondRix</h1>
    <section class="poster__details">
      <p>Saturday 25th November 2017</p>
      <p>Brisket Theatre,</p>
      <p>Holloway College Brambledale</p>
    </section>
  </main>
</body>
</html>
```